Wedding Thank You post card

We would like to design a thank you post card for our wedding guests.
We want it to be a classic style with our photo and a simple 'Thank you' written and then Tom and Sylvia 15.03.2014' Where the writing does not obstruct our image.
We need 140 post cards
Sorry for the delay please find some photos you can use for the design process. One or all photos can be used. Thank you
Wedding

```html
<!DOCTYPE html>
<html lang="en">
<head>
<meta charset="utf-8">
<title>Love &amp; Thanks Postcard – Tom and Sylvia</title>
<link rel="stylesheet" href="https://fonts.googleapis.com/css2?family=Sacramento&family=Libre+Baskerville&family=Open+Sans:wght@800&family=Questrial&display=swap">
<style>
  :root {
    --paper: #ffffff;
    --frame: #4a4a4a;
    --ink: #5f5f5f;
    --rule: #9a9a9a;
    --label: #555555;
    --overlay-text: #ffffff;
    --photo-warm-a: #c9a58c;
    --photo-warm-b: #e9e2dc;
    --photo-navy-a: #1f2b45;
    --photo-navy-b: #d8d6d8;
    --photo-pink-a: #d9548c;
    --photo-pink-b: #efe6ea;
    --photo-green-a: #6f9a48;
    --photo-green-b: #e7ecef;
  }
  * { margin: 0; padding: 0; box-sizing: border-box; }
  html, body { width: 1200px; height: 1173px; overflow: hidden; background: var(--paper); }
  .canvas { position: relative; width: 1200px; height: 1173px; }

  .side-label {
    position: absolute; left: 241px;
    font-family: "Questrial", sans-serif; font-size: 25px; color: var(--label);
  }
  .side-label--front { top: 22px; }
  .side-label--back { top: 600px; }

  .card {
    position: absolute; left: 237px; width: 721px; height: 528px;
    border: 1px solid var(--frame); background: var(--paper); overflow: hidden;
  }
  .card--front { top: 56px; }
  .card--back { top: 632px; }

  .photo {
    position: absolute; display: flex; align-items: center; justify-content: center;
    text-align: center; z-index: 2;
    font-family: "Open Sans", sans-serif; font-weight: 800; font-size: 32px; line-height: 1.2;
    color: var(--overlay-text); letter-spacing: 0.5px;
  }
  .photo--wide { width: 254px; height: 179px; }
  .photo--narrow { width: 156px; height: 179px; }
  .photo--couple-warm { background: linear-gradient(120deg, var(--photo-warm-a), var(--photo-warm-b) 55%, var(--photo-navy-a)); }
  .photo--bouquet { background: radial-gradient(circle at 50% 35%, var(--photo-pink-a), var(--photo-pink-b) 75%); }
  .photo--veil { background: linear-gradient(160deg, var(--photo-navy-b), #b7a9a6 50%, var(--photo-navy-a)); }
  .photo--lawn { background: linear-gradient(180deg, var(--photo-green-a), #c4c9bf 45%, var(--photo-navy-a) 75%, var(--photo-green-a)); }
  .photo--portrait { background: linear-gradient(160deg, #b08a72, var(--photo-navy-a) 70%); }
  .photo--smile { background: linear-gradient(120deg, #8a6a4e, var(--photo-green-b) 45%, var(--photo-navy-a)); }

  .swash { position: absolute; left: 0; top: 0; z-index: 1; }
  .headline {
    position: absolute; left: 0; width: 100%; top: 206px; height: 72px; text-align: center;
    font-family: "Sacramento", cursive; font-size: 92px; color: var(--ink);
    line-height: 72px; z-index: 1; white-space: nowrap;
  }
  .couple {
    position: absolute; text-align: center;
    font-family: "Libre Baskerville", serif; color: var(--ink); line-height: 21px;
  }
  .couple__names { font-size: 17px; letter-spacing: 0.5px; }
  .couple__date { font-size: 16px; }
  .couple--front { left: 0; width: 100%; top: 276px; }
  .couple--back { left: 40px; width: 238px; top: 32px; }

  .divider { position: absolute; left: 360px; top: 84px; width: 1px; height: 412px; background: var(--rule); }
  .stamp { position: absolute; left: 610px; top: 25px; width: 90px; height: 98px; border: 1px solid var(--rule); }
  .address-line { position: absolute; left: 394px; width: 274px; height: 1px; background: var(--rule); }
</style>
</head>
<body>
<div class="canvas">
  <div class="side-label side-label--front">front</div>

  <section class="card card--front">
    <div class="photo photo--wide photo--couple-warm" role="img" aria-label="Photo of the bride and groom" style="left:20px;top:21px;">YOUR PHOTO</div>
    <div class="photo photo--narrow photo--bouquet" role="img" aria-label="Photo of the bridal bouquet" style="left:282px;top:21px;">YOUR<br>PHOTO</div>
    <div class="photo photo--wide photo--veil" role="img" aria-label="Photo of the couple under the veil" style="left:446px;top:21px;">YOUR PHOTO</div>

    <svg class="swash" width="721" height="528" viewBox="0 0 721 528" aria-hidden="true">
      <path d="M0 260 C45 266 85 264 118 254" fill="none" stroke="var(--ink)" stroke-width="2"/>
      <path d="M612 244 C655 236 690 238 721 250" fill="none" stroke="var(--ink)" stroke-width="2"/>
    </svg>
    <div class="headline">love &amp; thanks</div>

    <div class="couple couple--front">
      <div class="couple__names">TOM AND SYLVIA</div>
      <div class="couple__date">March 15, 2014</div>
    </div>

    <div class="photo photo--wide photo--lawn" role="img" aria-label="Photo of the couple sitting on the lawn" style="left:20px;top:333px;">YOUR PHOTO</div>
    <div class="photo photo--narrow photo--portrait" role="img" aria-label="Portrait photo of the bride" style="left:282px;top:333px;">YOUR<br>PHOTO</div>
    <div class="photo photo--wide photo--smile" role="img" aria-label="Photo of the smiling couple" style="left:446px;top:333px;">YOUR PHOTO</div>
  </section>

  <div class="side-label side-label--back">back</div>

  <section class="card card--back">
    <div class="couple couple--back">
      <div class="couple__names">TOM AND SYLVIA</div>
      <div class="couple__date">March 15, 2014</div>
    </div>
    <div class="divider"></div>
    <div class="stamp"></div>
    <div class="address-line" style="top:322px;"></div>
    <div class="address-line" style="top:374px;"></div>
    <div class="address-line" style="top:428px;"></div>
  </section>
</div>
</body>
</html>
```